Simple+Professional tech feel + warm and friendly box design for pet test kit

Project Name: 10-Minute Canine & Feline Rapid Test Kit Packaging Design
Target Brand Reference: VETRALUX (South Korea) styles
Design Style Direction: Professional tech feel + warm and friendly
Professionalism (Professional): Clear typography and distinct information hierarchy to reflect the product’s scientific rigor and accuracy.
Technological: Reflected through clean graphics and a minimalist layout.
Friendly: Utilise soft, warm colour combinations to convey care for pets and well-wishes for their health.
International: The design should align with mainstream aesthetics and avoid cultural ambiguities.

Target Market(s)
European Union and the United States
Industry/Entity Type
Veterinary Medical
Look and feel
Each slider illustrates characteristics of the customer's brand and the style your logo design should communicate.

```html
<!DOCTYPE html>
<html lang="en">
<head>
<meta charset="utf-8">
<title>ClaroPet Rapid Test Kit Packaging</title>
<link href="https://fonts.googleapis.com/css2?family=Montserrat:wght@400;600;700;800&display=swap" rel="stylesheet">
<style>
  :root{
    --green:#66b22a;
    --green-soft:#8cc95c;
    --white:#f4f4f4;
    --ink:#1f1f1f;
    --grey:#b9b9b9;
    --bg:#e6e6e6;
  }
  *{box-sizing:border-box;margin:0;padding:0}
  html,body{width:1200px;height:912px;overflow:hidden;background:var(--bg);font-family:"Montserrat",sans-serif;color:var(--ink)}
  .stage{position:relative;width:1200px;height:912px}
  .panel{position:absolute;background:var(--white);overflow:hidden}
  .lid-band{position:absolute;left:0;right:0;top:0;height:26px;background:var(--green);display:flex;align-items:center;justify-content:center}
  .lid-band span{color:var(--green-soft);font-weight:800;font-size:16px;letter-spacing:1px;transform:scaleY(-1)}
  .foot-band{position:absolute;left:0;right:0;bottom:0;height:58px;background:var(--green);display:flex;align-items:center;padding:0 22px}
  .brand-name{font-weight:700;letter-spacing:.5px}
  .brand-name sup{font-size:.35em;font-weight:600;vertical-align:top;margin-left:2px}
  .maker-name{color:#fff;font-weight:700;font-size:18px;letter-spacing:.5px}

  .top-panel{left:429px;top:210px;width:332px;height:176px;background:var(--green);display:flex;align-items:center;justify-content:center}
  .top-panel .brand-name{color:#fff;font-size:42px}

  .front{left:52px;top:428px;width:364px;height:247px}
  .front .brand-name{position:absolute;left:26px;top:42px;font-size:32px}
  .front .product-lines{position:absolute;left:27px;top:133px;font-size:11px;line-height:12px}
  .front .product-lines b{font-weight:700}
  .pet-art{position:absolute;left:182px;top:55px;width:150px;height:150px;border-radius:70px 70px 20px 20px;background:linear-gradient(160deg,#dcefcc,#b9de98)}
  .front .foot-band{justify-content:flex-end;padding-right:40px}

  .side-a{left:424px;top:428px;width:165px;height:247px}
  .note-pill{position:absolute;left:7px;top:62px;width:151px;height:40px;border-radius:6px;background:var(--green);color:#f0f8e8;font-size:8.5px;line-height:10px;padding:5px 6px}
  .contact{position:absolute;left:11px;top:124px;font-size:8.5px;line-height:9.5px}
  .contact b{font-weight:700}
  .side-a .foot-band{padding:0 14px;gap:10px}
  .icon-row{display:flex;align-items:center;gap:8px}
  .icon-row svg{display:block}
  .ivd{border:1px solid #fff;color:#fff;font-size:8px;padding:1px 4px}
  .temp{color:#fff;font-size:7px;line-height:9px}

  .back{left:613px;top:428px;width:345px;height:247px}
  .back .brand-name{position:absolute;left:20px;top:42px;font-size:32px}
  .sticker{position:absolute;left:19px;top:85px;width:306px;height:92px;border-radius:10px;background:var(--grey);display:flex;align-items:center;justify-content:center;font-size:28px;font-weight:400}
  .back .foot-band{justify-content:space-between}
  .count{display:flex;align-items:center;color:#fff}
  .count strong{font-size:28px;font-weight:700;line-height:1}
  .count span{font-size:10px;line-height:10px;margin-left:2px}
  .pet-mini{width:56px;height:44px;border-radius:24px 24px 8px 8px;background:var(--green-soft)}

  .side-b{left:954px;top:428px;width:182px;height:247px}
  .story{position:absolute;left:26px;top:63px;width:130px;text-align:center;font-size:8.5px;line-height:9px}
  .side-b .foot-band{justify-content:center}
  .side-b .brand-name{color:#fff;font-size:22px}
</style>
</head>
<body>
<main class="stage">

  <section class="panel top-panel" aria-label="Box top">
    <div class="brand-name">ClaroPet<sup>TM</sup></div>
  </section>

  <section class="panel front" aria-label="Box front">
    <div class="lid-band"><span>ClaroPet</span></div>
    <div class="brand-name">ClaroPet<sup>TM</sup></div>
    <div class="pet-art" role="img" aria-label="Line illustration of a sitting dog and cat"></div>
    <p class="product-lines"><b>10-Minute</b> Canine &amp; Feline<br><b>Rapid Test Kit</b><br>For Dogs and Cat</p>
    <div class="foot-band"><span class="maker-name">NORVELLE</span></div>
  </section>

  <section class="panel side-a" aria-label="Box side with contact details">
    <div class="lid-band"><span>ClaroPet</span></div>
    <div class="note-pill">(For accurate results, please read the instructions carefully before use)</div>
    <p class="contact">A Clear View into Pet Health<br>Made by Norvelle<br>Norvelle Biotech Limited<br>Web:<b>www.norvelle-bio.com</b><br>E-mail:sales@norvelle-bio.com</p>
    <div class="foot-band">
      <div class="icon-row">
        <svg width="16" height="16" viewBox="0 0 16 16"><circle cx="8" cy="8" r="7" fill="none" stroke="#fff" stroke-width="1.3"/><text x="8" y="11.5" font-size="10" text-anchor="middle" fill="#fff" font-family="Montserrat,sans-serif">2</text></svg>
        <svg width="16" height="16" viewBox="0 0 16 16"><path d="M2 8a6 6 0 0 1 12 0z" fill="#fff"/><path d="M8 8v5a1.5 1.5 0 0 1-3 0" fill="none" stroke="#fff" stroke-width="1.2"/></svg>
        <svg width="16" height="16" viewBox="0 0 16 16"><circle cx="8" cy="8" r="3" fill="none" stroke="#fff" stroke-width="1.2"/><path d="M8 1v3M8 12v3M1 8h3M12 8h3M3 3l2 2M11 11l2 2M13 3l-2 2M5 11l-2 2" stroke="#fff" stroke-width="1.1"/></svg>
        <span class="ivd">IVD</span>
        <svg width="12" height="22" viewBox="0 0 12 22"><path d="M6 2v14" stroke="#fff" stroke-width="2"/><circle cx="6" cy="18" r="3" fill="#fff"/></svg>
        <span class="temp">30°C<br>4°C</span>
      </div>
    </div>
  </section>

  <section class="panel back" aria-label="Box back">
    <div class="lid-band"><span>ClaroPet</span></div>
    <div class="brand-name">ClaroPet<sup>TM</sup></div>
    <div class="sticker">(Sticker)</div>
    <div class="foot-band">
      <div class="count"><strong>5</strong><span>TESTS<br>KIT</span></div>
      <div class="pet-mini" role="img" aria-label="Small line illustration of a dog and cat"></div>
      <span class="maker-name">NORVELLE</span>
    </div>
  </section>

  <section class="panel side-b" aria-label="Box side with brand story">
    <div class="lid-band"><span>ClaroPet</span></div>
    <p class="story">"ClaroPet is made by Norvelle, our name combines 'Nor' for innovation with 'Velle' from philosophy, representing both intelligent efficacy in our science and reverence for the spirit of life ('Wan Wu You Ling') in all creatures</p>
    <div class="foot-band"><div class="brand-name">ClaroPet<sup>TM</sup></div></div>
  </section>

</main>
</body>
</html>
```